Postcard Design Project

We sells Laser Printer Ink and Toners, We also sells on Zephra Market Place, Need a post card for these zephra contact to start buying through our website instead of Zephra. Company Name: Kv Business Supplies LLC, website is www.kvtoner.example phone#555-203-4471

```html
<!DOCTYPE html>
<html lang="en">
<head>
<meta charset="utf-8">
<title>Kv Business Supplies – Postcard</title>
<link rel="stylesheet" href="https://fonts.googleapis.com/css2?family=Roboto+Slab:wght@800;900&family=Cabin:wght@400;500;700&family=Open+Sans:wght@400&display=swap">
<style>
:root{
  --stage:#e2e2e2;
  --paper:#ffffff;
  --ink:#111111;
  --cyan:#1aa3e0;
  --blue:#1e7fd0;
  --purple:#5b2d8e;
  --magenta:#e0197d;
  --orange:#f7931e;
  --red:#d9262c;
  --yellow:#ffe82a;
  --white:#ffffff;
}
*{margin:0;padding:0;box-sizing:border-box}
html,body{width:1200px;height:640px;overflow:hidden;background:var(--stage)}
.stage{position:relative;width:1200px;height:640px}
.postcard{position:absolute;background:var(--paper);overflow:hidden;transform-origin:0 0;transform:scale(.8);box-shadow:3px 4px 8px rgba(0,0,0,.18)}
.postcard--front{left:81px;top:163px;width:608px;height:438px}
.postcard--back{left:616px;top:163px;width:618px;height:448px}
.postcard svg.art{position:absolute;left:0;top:0}
.brand{position:absolute;display:flex;align-items:center;gap:8px;font-family:'Cabin',sans-serif;font-weight:700;color:var(--ink);white-space:nowrap}
.brand__mark{background:var(--magenta);border-radius:4px;flex:none}
.headline{position:absolute;font-family:'Roboto Slab',serif;font-weight:900;color:var(--ink);white-space:nowrap}
.tag{position:absolute;font-family:'Open Sans',sans-serif;color:var(--cyan);white-space:nowrap}
.copy{position:absolute;font-family:'Cabin',sans-serif;color:var(--white)}
.copy .hi{color:var(--yellow)}
.url,.phone{font-weight:700;white-space:nowrap}
/* front */
.front-brand{left:12px;top:44px;font-size:17px}
.front-brand .brand__mark{width:28px;height:28px}
.front-head{left:215px;top:16px;width:380px;font-size:27px;line-height:34px;text-align:center}
.front-tag{left:215px;width:380px;text-align:center;top:89px;font-size:16px}
.front-offer{left:25px;top:175px;width:190px;font-size:18px;line-height:25px}
.front-offer .lead{font-size:23px;display:block}
.front-web{left:25px;top:325px;color:var(--yellow);font-weight:700}
.front-web .label{font-size:17px;display:block}
.front-web .url{font-size:26px}
.front-call{left:455px;top:352px;color:var(--yellow);font-family:'Roboto Slab',serif;font-weight:900;transform:rotate(5deg);transform-origin:0 0;line-height:1.15;white-space:nowrap}
.front-call .label{font-size:18px;display:block}
.front-call .phone{font-size:21px;font-weight:900}
/* back */
.back-brand{left:8px;top:14px;font-size:11px;gap:6px}
.back-brand .brand__mark{width:22px;height:22px}
.back-head{left:148px;top:22px;font-size:14px;line-height:18px}
.back-head .l2{padding-left:36px;display:block}
.back-tech{left:12px;top:311px;font-family:'Roboto Slab',serif;font-weight:900;color:var(--yellow);font-size:12px;white-space:nowrap}
.back-offer{left:12px;top:330px;font-size:11px;line-height:14px;width:280px}
.back-offer .lead{font-size:14px}
.back-contact{left:14px;top:388px;font-size:10px;line-height:14px}
.back-contact .phone{font-size:12px}
.back-contact .url{font-size:13px}
</style>
</head>
<body>
<div class="stage">

  <section class="postcard postcard--front">
    <svg class="art" width="608" height="438" viewBox="0 0 608 438">
      <defs>
        <linearGradient id="f-panel" x1="0" y1="0" x2="0.3" y2="1">
          <stop offset="0" stop-color="#5b2d8e"/><stop offset=".45" stop-color="#2a8fd8"/><stop offset="1" stop-color="#1f6fc0"/>
        </linearGradient>
        <linearGradient id="f-band" x1="0" y1="0" x2="1" y2="0">
          <stop offset="0" stop-color="#fbe3c8"/><stop offset=".5" stop-color="#f7931e"/><stop offset="1" stop-color="#d9262c"/>
        </linearGradient>
        <linearGradient id="f-pink" x1="0" y1="0" x2="0" y2="1">
          <stop offset="0" stop-color="#e0197d"/><stop offset=".5" stop-color="#f59ac8"/><stop offset="1" stop-color="#e0197d"/>
        </linearGradient>
        <linearGradient id="f-photo" x1="0" y1="0" x2="1" y2="1">
          <stop offset="0" stop-color="#5c636b"/><stop offset=".6" stop-color="#c9ced4"/><stop offset="1" stop-color="#eef1f4"/>
        </linearGradient>
        <linearGradient id="f-orange" x1="0" y1="0" x2="1" y2="0">
          <stop offset="0" stop-color="#fbe3c8"/><stop offset="1" stop-color="#f7931e"/>
        </linearGradient>
      </defs>
      <path d="M290,165 Q450,160 608,190 L608,345 L290,345 Z" fill="url(#f-photo)" role="img" aria-label="Photo of a technician servicing a laser printer toner cartridge"/>
      <path d="M0,118 L188,94 L320,350 L345,410 Q160,418 0,438 Z" fill="url(#f-panel)"/>
      <path d="M180,112 Q400,100 608,140 L608,152 Q400,114 186,122 Z" fill="#1aa3e0"/>
      <path d="M188,125 Q400,118 608,158 L608,180 Q400,140 200,145 Z" fill="url(#f-band)"/>
      <path d="M200,140 L365,152 L298,338 Z" fill="url(#f-pink)"/>
      <path d="M292,350 L440,360 L430,405 L330,402 Z" fill="url(#f-orange)"/>
      <path d="M445,352 L608,338 L608,418 L432,420 Z" fill="#1aa3e0"/>
    </svg>

    <div class="brand front-brand"><span class="brand__mark"></span>Kv Business Supplies</div>
    <h1 class="headline front-head">START BUYING THROUGH<br>OUR WEBSITE</h1>
    <p class="tag front-tag">GET A TECHNICIAN IN YOUR OFFICE TODAY</p>
    <p class="copy front-offer"><span class="hi lead">Free Shipping on</span>$50.00 or more as an Orvel Partner they are qualified for Orvel Rebates. $25-$50.</p>
    <p class="copy front-web"><span class="label">Visit us online</span><span class="url">www.kvtoner.example</span></p>
    <p class="copy front-call"><span class="label">CALL TODAY</span><span class="phone">555-203-4471</span></p>
  </section>

  <section class="postcard postcard--back">
    <svg class="art" width="618" height="448" viewBox="0 0 618 448">
      <defs>
        <linearGradient id="b-band" x1="0" y1="0" x2="1" y2="0">
          <stop offset="0" stop-color="#f7931e"/><stop offset="1" stop-color="#d9262c"/>
        </linearGradient>
        <linearGradient id="b-photo" x1="0" y1="0" x2="1" y2="1">
          <stop offset="0" stop-color="#cfe3f2"/><stop offset=".5" stop-color="#7fd3e6"/><stop offset="1" stop-color="#2a2d31"/>
        </linearGradient>
        <linearGradient id="b-pink" x1="0" y1="0" x2="1" y2="0">
          <stop offset="0" stop-color="#f26bb0"/><stop offset="1" stop-color="#e0197d"/>
        </linearGradient>
        <linearGradient id="b-panel" x1="0" y1="0" x2="1" y2="0.4">
          <stop offset="0" stop-color="#5b2d8e"/><stop offset=".45" stop-color="#1aa3e0"/><stop offset="1" stop-color="#1e7fd0"/>
        </linearGradient>
      </defs>
      <path d="M0,95 Q160,88 308,104 L308,290 L0,290 Z" fill="url(#b-photo)" role="img" aria-label="Close-up photo of a laser toner cartridge drum"/>
      <path d="M0,66 Q160,58 308,72 L308,80 Q160,66 0,74 Z" fill="#1e7fd0"/>
      <path d="M0,76 Q160,68 308,82 L308,104 Q160,88 0,98 Z" fill="url(#b-band)"/>
      <path d="M0,258 Q150,250 308,272 L308,292 Q150,270 0,278 Z" fill="url(#b-pink)"/>
      <path d="M0,278 Q150,270 308,292 L308,448 L0,448 Z" fill="url(#b-panel)"/>
    </svg>

    <div class="brand back-brand"><span class="brand__mark"></span>Kv Business Supplies</div>
    <h2 class="headline back-head">START BUYING THROUGH<span class="l2">OUR WEBSITE</span></h2>
    <p class="copy back-tech">GET A TECHNICIAN IN YOUR OFFICE TODAY</p>
    <p class="copy back-offer"><span class="hi lead">Free Shipping on</span> $50.00 or more as an<br>Orvel Partner they are qualified for<br>Orvel Rebates. $25-$50.</p>
    <p class="copy back-contact">CALL TODAY<br><span class="phone">555-203-4471</span><br>Visit us online<br><span class="url">www.kvtoner.example</span></p>
  </section>

</div>
</body>
</html>
```